Birthday Party Invitation for Jasper's 18th Birthday Party

Our eldest son Jasper is turning 18 and we are having a party at home to celebrate the occasion. This project is about creating an invitation that will go to our friends and family. We like things to be nicely designed so posting it to pixel harbor seemed to be the way to go.
The invitation needs to be able to be printed onto an A4 piece of paper. We have access to a color copier so it can be nice and bright.

We want an invitation that conveys a sense of occasion and looks as though we have put time and effort into having a great night to celebrate his 18th.
I have included some photo's of Jasper. They can go onto the invitation as is or they can be given some treatment to form a theme when on the invitiation. I'll leave the treatment of the photo's to the individual designer.

Target Market(s)

Friends and Family

Font styles to use
Sans Serif

Colors

Designer to choose colors to be used in the design.

Requirements
Must have
• The invitation must have the time, date and location of the party.
• Details:
• Saturday 29th of July 2017 7.00pm
• 41 Brackmere Lane, Fenwood
• Food and Drinks provided It must be bright and colourful and convey a sense of excitement.
Nice to have
• Inclusion of the photo's that I have uploaded.
Should not have
• any boring bits

```html
<!DOCTYPE html>
<html lang="en">
<head>
<meta charset="utf-8">
<title>Jasper's 18th Birthday Invitation</title>
<link rel="stylesheet" href="https://fonts.googleapis.com/css2?family=Cinzel:wght@700;900&family=Montserrat:wght@500&family=Old+Standard+TT&display=swap">
<style>
  :root {
    --navy: #25285e;
    --royal: #1f2a7a;
    --azure: #1e6bb8;
    --gold-light: #f3e2b0;
    --gold-mid: #d9bd7c;
    --gold-dark: #a78646;
    --plum: #3b3a7c;
    --plum-light: #5a5f9e;
    --wine: #5a1a1a;
  }
  * { margin: 0; padding: 0; box-sizing: border-box; }
  html, body { width: 1200px; height: 849px; overflow: hidden; background: #fff; }
  .invitation { position: relative; width: 1200px; height: 849px; overflow: hidden; }

  .header-band {
    position: absolute; left: 0; top: 0; width: 1200px; height: 184px;
    background: linear-gradient(90deg, #c9ae6f 0%, var(--gold-light) 45%, var(--gold-mid) 75%, #c6a866 100%);
    display: flex; flex-direction: column; align-items: center; justify-content: center;
  }
  .headline {
    font-family: "Cinzel", serif; font-weight: 900; color: var(--navy);
    font-size: 38px; line-height: 52px; text-align: center; letter-spacing: 0.5px;
  }
  .headline sup { font-size: 20px; vertical-align: 14px; }

  .gold-rule {
    position: absolute; left: 0; width: 1200px; height: 12px;
    background: linear-gradient(180deg, var(--gold-dark), var(--gold-light) 50%, var(--gold-dark));
  }
  .gold-rule.upper { top: 184px; }
  .gold-rule.lower { top: 620px; }

  .photo-band {
    position: absolute; left: 0; top: 196px; width: 1200px; height: 424px;
    background: radial-gradient(ellipse 55% 90% at 52% 45%, var(--azure) 0%, #1d4c9e 45%, var(--royal) 100%);
  }

  .photo-frame {
    position: absolute;
    background: linear-gradient(135deg, var(--gold-dark), var(--gold-light) 45%, var(--gold-mid) 70%, var(--gold-dark));
    padding: 12px;
    box-shadow: 0 2px 6px rgba(0,0,0,0.35);
  }
  .photo-frame .photo { width: 100%; height: 100%; border: 3px solid var(--royal); }
  .frame-portrait { left: 25px; top: 238px; width: 337px; height: 339px; padding: 13px; }
  .frame-small { top: 281px; width: 252px; height: 252px; padding: 8px; }
  .frame-harbour { left: 391px; }
  .frame-family { left: 657px; }
  .frame-friend { left: 923px; }

  .photo-school { background: linear-gradient(180deg, #8fb6d8 0%, #7f9a6a 45%, #2a2530 100%); }
  .photo-harbour { background: linear-gradient(180deg, #b7c7d6 0%, #6f8aa0 40%, #3c3f52 100%); }
  .photo-family { background: linear-gradient(180deg, #6b4a40 0%, #6c8a5a 40%, #3d4a6c 100%); }
  .photo-friend { background: linear-gradient(180deg, #4e6a3c 0%, #9aa78f 50%, #8a8aa2 100%); }

  .details-band {
    position: absolute; left: 0; top: 632px; width: 1200px; height: 217px;
    background: linear-gradient(90deg, var(--plum) 0%, var(--plum-light) 50%, var(--plum) 100%);
  }

  .details-card {
    position: absolute; left: 268px; top: 666px; width: 664px; height: 140px;
    border-radius: 9px;
    background: linear-gradient(90deg, #c9ad6c 0%, var(--gold-light) 45%, var(--gold-mid) 80%, #c7a967 100%);
    text-align: center; padding-top: 20px;
  }
  .details-line {
    font-family: "Montserrat", sans-serif; font-weight: 500; color: var(--navy);
    font-size: 26px; line-height: 37px;
  }
  .details-note {
    font-family: "Old Standard TT", serif; color: var(--wine);
    font-size: 25px; line-height: 38px; letter-spacing: 0.5px;
    transform: scaleX(0.88); display: inline-block;
  }
</style>
</head>
<body>
<main class="invitation">
  <header class="header-band">
    <h1 class="headline">Please join us for a celebration<br>in honor of Jasper’s 18<sup>th</sup> year!</h1>
  </header>
  <div class="gold-rule upper"></div>

  <section class="photo-band"></section>
  <figure class="photo-frame frame-portrait">
    <div class="photo photo-school" role="img" aria-label="Portrait of Jasper in a striped school blazer beside a river"></div>
  </figure>
  <figure class="photo-frame frame-small frame-harbour">
    <div class="photo photo-harbour" role="img" aria-label="Jasper smiling at the harbour with a bridge behind him"></div>
  </figure>
  <figure class="photo-frame frame-small frame-family">
    <div class="photo photo-family" role="img" aria-label="Jasper in a tuxedo with his parents in a garden"></div>
  </figure>
  <figure class="photo-frame frame-small frame-friend">
    <div class="photo photo-friend" role="img" aria-label="Jasper with a friend in a garden"></div>
  </figure>

  <div class="gold-rule lower"></div>
  <section class="details-band"></section>
  <div class="details-card">
    <p class="details-line">Saturday | 29th of July 2017 | 7:00 PM</p>
    <p class="details-line">41 Brackmere Lane, Fenwood</p>
    <p class="details-note">Food and Drinks provided</p>
  </div>
</main>
</body>
</html>
```